Webdesign für Seminaranbieter
Zielgruppe
Die Velkor Academy bietet Kurse, Seminare & Coachings im Bereich der Kommunikation / Persönlichkeitsentwicklung an.
Folgendes Angebot besteht zur Zeit:
Seminare:
- 'Erste Schritte Dialog', eine Einführung in die Kommunikation.
- 'Sonnige Tage, ruhige Abende' zum Thema Erziehung.
- 'Zeitenwende im Herbst', zum Thema Älter werden und den Umgang damit.
Kurse:
- 'Gewaltfreie Kommunikation', Übungsgruppe
Coaching:
- Einzelsitzungen mit Hypnose
Ps: im Anhang unter 'Angabot_Vorlage.pdf' finden Sie mehr Infos zu den einezlenen Angebote.
Aufgabenstellung
Bitte berücksichtigen Sie, dass bereits ein Logo besteht (siehe Anhang).
Vom gesamteindruck her sollte die Website aufgeräumt, übersichtlich, harmonisch, freundlich & frisch wirken.
Es wäre super, wenn die Website authentisch wirkt (und weniger '0815 Business Website').
Bitte bedenken Sie, dass die Website sich an Private richtet, die sich nach einem 'strahlenderen & unbeschwerterem Lebene sehnen'.
Wir haben bereits viele Persönlichkeiten stärken können und möchten dies auch witerhin mit viel Herzblut machen.

```html
<!DOCTYPE html>
<html lang="de">
<head>
<meta charset="utf-8">
<title>Velkor Academy – Kontakt</title>
<link href="https://fonts.googleapis.com/css2?family=Raleway:wght@400;500;600&display=swap" rel="stylesheet">
<style>
  :root {
    --page-bg: #ede6e0;
    --panel: #ffffff;
    --band: #f0bb88;
    --accent: #f47148;
    --heading: #5e4f70;
    --text: #555158;
    --field-line: #b9b4b6;
    --placeholder: #8a8589;
    --footer-bar: #9a8878;
    --dark: #2e2a2c;
  }
  * { box-sizing: border-box; margin: 0; padding: 0; }
  html, body { width: 704px; height: 1200px; overflow: hidden; }
  body {
    position: relative;
    background: var(--page-bg);
    font-family: "Raleway", sans-serif;
    color: var(--text);
  }
  .panel { position: absolute; left: 79px; top: 45px; width: 551px; height: 1093px; background: var(--panel); }
  .abs { position: absolute; }

  /* Header */
  .site-header { position: absolute; left: 79px; top: 45px; width: 551px; height: 35px; background: #f3f3f6; }
  .brand { position: absolute; left: 18px; top: 12px; font-size: 7px; font-weight: 500; letter-spacing: 1px; color: var(--dark); }
  .nav { position: absolute; top: 12px; font-size: 5.5px; letter-spacing: .3px; color: var(--dark); }
  .nav.active { border: 1px solid var(--accent); color: var(--accent); padding: 3px 6px; top: 9px; }

  /* Hero */
  .hero {
    position: absolute; left: 79px; top: 80px; width: 551px; height: 287px;
    background:
      radial-gradient(ellipse 120px 110px at 52% 40%, #8a9ad8 0%, #aab4e0 55%, rgba(200,205,230,0) 100%),
      radial-gradient(ellipse 220px 140px at 50% 70%, #e6c6b4 0%, rgba(230,198,180,0) 100%),
      linear-gradient(90deg, #efe4b8 0%, #dcdbe6 25%, #dcdde9 75%, #efe6bc 100%);
  }
  .hero-title { position: absolute; left: 0; width: 551px; top: 163px; text-align: center; color: #fff; font-size: 22px; font-weight: 500; letter-spacing: 3px; }
  .hero-tagline { position: absolute; left: 0; width: 551px; top: 197px; text-align: center; color: #fff; font-size: 11.5px; font-weight: 500; letter-spacing: 1px; }
  .slider-arrow { position: absolute; top: 195px; }
  .dots { position: absolute; top: 272px; left: 262px; display: flex; gap: 3px; }
  .dot { width: 5px; height: 5px; border: 1px solid #fff; border-radius: 50%; }
  .dot.current { background: #fff; }

  /* Newsletter band */
  .newsletter { position: absolute; left: 78px; top: 376px; width: 550px; height: 37px; background: var(--band); }
  .newsletter-title { position: absolute; left: 80px; top: 10px; color: #fff; font-size: 7.5px; font-weight: 600; letter-spacing: 1px; }
  .newsletter-sub { position: absolute; left: 80px; top: 20px; color: #fff; font-size: 7.5px; font-weight: 500; }
  .newsletter-input { position: absolute; left: 239px; top: 9px; width: 193px; height: 19px; background: #fff; border: 1px solid #d9d0c8; font-size: 6.5px; letter-spacing: .8px; color: var(--placeholder); padding: 6px 7px; }
  .newsletter-ok { position: absolute; left: 441px; top: 12px; width: 22px; height: 14px; background: var(--accent); color: #fff; font-size: 6.5px; font-weight: 600; text-align: center; line-height: 14px; letter-spacing: .8px; }

  /* Contact form */
  .form-heading { position: absolute; left: 158px; top: 451px; font-size: 15px; font-weight: 500; letter-spacing: .8px; color: var(--heading); }
  .field { position: absolute; border: 1px solid var(--field-line); font-size: 6.5px; letter-spacing: .8px; color: var(--placeholder); padding: 6px 9px; background: #fff; }
  .checkbox { position: absolute; left: 159px; top: 650px; width: 15px; height: 15px; border: 1px solid var(--field-line); }
  .checkbox-label { position: absolute; left: 178px; top: 655px; font-size: 6.5px; letter-spacing: .6px; color: var(--placeholder); }
  .button { position: absolute; background: var(--accent); color: #fff; font-size: 7px; font-weight: 500; letter-spacing: 1px; text-align: center; }

  /* Landscape band */
  .landscape {
    position: absolute; left: 78px; top: 733px; width: 550px; height: 154px;
    background: linear-gradient(180deg, #ccd0d6 0%, #d6d6d8 40%, #a89c94 70%, #4a3e38 100%);
  }

  /* Footer */
  .footer-brand { position: absolute; left: 94px; width: 200px; top: 952px; text-align: center; font-size: 9.5px; font-weight: 500; letter-spacing: 2px; color: var(--dark); }
  .footer-info { position: absolute; left: 94px; width: 200px; text-align: center; font-size: 7.5px; line-height: 9.5px; color: var(--text); }
  .footer-info.company { font-weight: 600; letter-spacing: .4px; }
  .footer-question { position: absolute; left: 365px; top: 904px; font-size: 7.5px; line-height: 9.5px; letter-spacing: .6px; color: var(--dark); }
  .bottom-bar { position: absolute; left: 77px; top: 1092px; width: 551px; height: 46px; background: var(--footer-bar); }
  .bottom-link { position: absolute; top: 20px; font-size: 7.5px; letter-spacing: .4px; color: #fff; }
</style>
</head>
<body>
  <div class="panel"></div>

  <header class="site-header">
    <div class="brand">VELKOR ACADEMY</div>
    <span class="nav" style="left:384px">HOME</span>
    <span class="nav" style="left:419px">ANGEBOT</span>
    <span class="nav active" style="left:452px">KONTAKT</span>
    <span class="nav" style="left:496px">ÜBER UNS</span>
  </header>

  <section class="hero" role="img" aria-label="Foto: zwei Hände halten eine gläserne Weltkugel">
    <svg class="slider-arrow" style="left:12px" width="14" height="24" viewBox="0 0 14 24"><polyline points="12,1 2,12 12,23" fill="none" stroke="#fff" stroke-width="1"/></svg>
    <svg class="slider-arrow" style="left:525px" width="14" height="24" viewBox="0 0 14 24"><polyline points="2,1 12,12 2,23" fill="none" stroke="#fff" stroke-width="1"/></svg>
    <div class="hero-title">VELKOR ACADEMY</div>
    <div class="hero-tagline">NEUE PERSPECTIVEN • NEUE HORIZONTE</div>
    <div class="dots"><span class="dot"></span><span class="dot"></span><span class="dot current"></span></div>
  </section>

  <section class="newsletter">
    <div class="newsletter-title">KOSTENLOSES ERSTGESPRÄCH</div>
    <div class="newsletter-sub">Abonnieren Sie unseren Newsletter!</div>
    <div class="newsletter-input">E-MAIL ADRESSE</div>
    <div class="newsletter-ok">OK</div>
  </section>

  <h1 class="form-heading">WIR FREUEN UNS ÜBER IHRE ANFRAGE</h1>
  <div class="field" style="left:158px;top:493px;width:322px;height:90px">NACHRICHT</div>
  <div class="field" style="left:158px;top:600px;width:143px;height:19px">NAME</div>
  <div class="field" style="left:335px;top:600px;width:145px;height:19px;padding-left:7px">VORNAME</div>
  <div class="field" style="left:158px;top:625px;width:322px;height:19px">E-MAIL ADRESSE</div>
  <div class="checkbox"></div>
  <div class="checkbox-label">Kopie an meine E-Mail Adresse senden</div>
  <div class="button" style="left:158px;top:692px;width:66px;height:16px;line-height:16px">SENDEN</div>

  <div class="landscape" role="img" aria-label="Foto: Person sitzt auf einem Felsvorsprung über einem weiten Bergtal im Gegenlicht"></div>

  <div class="footer-brand">VELKOR ACADEMY</div>
  <div class="footer-info company" style="top:988px">VELKOR ACADEMY GMBH.</div>
  <div class="footer-info" style="top:1007px">Lindenweg 42<br>5678 Talbrunn</div>
  <div class="footer-info" style="top:1035px">TEL: 0155 987 321<br>hallo@velkoracademy.ch</div>

  <div class="footer-question">NOCH FRAGEN, ANREGUNGEN?<br>SCHREIBEN SIE UNS!</div>
  <div class="field" style="left:365px;top:932px;width:193px;height:19px">NAME</div>
  <div class="field" style="left:364px;top:958px;width:194px;height:19px;padding-left:7px">E-MAIL ADRESSE</div>
  <div class="field" style="left:364px;top:983px;width:194px;height:60px;padding-left:7px">NACHRICHT</div>
  <div class="button" style="left:365px;top:1051px;width:96px;height:21px;line-height:21px">SENDEN</div>

  <footer class="bottom-bar">
    <span class="bottom-link" style="left:34px">Datenschutz</span>
    <span class="bottom-link" style="left:104px">Impressum</span>
    <span class="bottom-link" style="left:234px">VELKOR ACADEMY | 2019</span>
  </footer>
</body>
</html>
```